I need to rebrand my public user portal for a new/modern look and feel

I want to take my current user web portal and redesign the look of it. I have included 2 samples of my current user portal and would like options to create a new functional look. This main page below will modify based on the tabs on the top left. Any questions please ask.

```html
<!DOCTYPE html>
<html lang="en">
<head>
<meta charset="utf-8">
<title>Northfield Learning – Portal Dashboard</title>
<link href="https://fonts.googleapis.com/css2?family=Montserrat:wght@400;500;600;700&display=swap" rel="stylesheet">
<style>
:root{
  --stage:#8a8a8a;
  --screen:#ece4f8;
  --white:#ffffff;
  --ink:#2b2b33;
  --brand:#6a23d6;
  --side-top:#8b48d2;
  --side-bottom:#1e0a78;
  --card-top:#f1e9fc;
  --card-bottom:#ccb3ef;
  --card-line:#d3c2ee;
  --row-tint:#dccaf4;
  --head-tint:#c9adf0;
  --mark:#7c1620;
}
*{box-sizing:border-box;margin:0;padding:0}
html,body{width:728px;height:1200px;overflow:hidden;background:var(--stage);font-family:"Montserrat",sans-serif;color:var(--ink)}
.viewport{position:relative;width:728px;height:1200px;overflow:hidden}
.stage{position:absolute;left:0;top:0;width:1495px;height:2464px;transform:scale(0.48696);transform-origin:0 0;overflow:hidden}
.icon-defs{position:absolute;width:0;height:0;overflow:hidden}
.screen{position:absolute;left:103px;width:1289px;height:1103px;background:var(--screen);overflow:hidden}
.screen--one{top:101px}
.screen--two{top:1259px}

.sidebar{position:absolute;left:28px;top:29px;width:260px;height:962px;border-radius:16px;background:linear-gradient(180deg,var(--side-top) 0%,#5a1eb8 35%,var(--side-bottom) 100%)}
.nav-item{position:absolute;left:9px;width:251px;height:43px;display:flex;align-items:center;padding-left:27px;gap:16px;color:var(--white);font-size:16px;white-space:nowrap}
.nav-item svg{width:20px;height:20px;fill:currentColor;flex:none}
.nav-item--active{background:var(--white);color:var(--brand);border-radius:22px 0 0 22px}

.topbar{position:absolute;left:40px;top:39px;width:1232px;height:104px;background:var(--white);border-radius:14px;box-shadow:0 4px 14px rgba(90,40,160,.12)}
.brand{position:absolute;left:30px;top:34px;display:flex;align-items:center;gap:10px;color:var(--mark);font-weight:700;font-size:26px;white-space:nowrap}
.brand-square{width:34px;height:34px;background:var(--mark)}
.search{position:absolute;left:467px;top:28px;width:500px;height:48px;border:1.5px solid #9a9aa2;border-radius:24px;display:flex;align-items:center;padding-left:31px;font-size:17px;color:#444}
.search-btn{position:absolute;right:6px;top:7px;width:32px;height:32px;border-radius:50%;background:var(--brand);color:var(--white);display:flex;align-items:center;justify-content:center}
.search-btn svg{width:16px;height:16px}
.avatar{position:absolute;left:1004px;top:19px;width:66px;height:66px;border-radius:50%;background:linear-gradient(160deg,#b9b4ae,#4a4d57)}
.user{position:absolute;left:1085px;top:40px;font-size:19px;font-weight:500}
.caret{position:absolute;left:1180px;top:49px;width:0;height:0;border-left:7px solid transparent;border-right:7px solid transparent;border-top:8px solid #111}

.card{position:absolute;left:308px;width:960px;border:1px solid var(--card-line);border-radius:12px;background:linear-gradient(180deg,var(--card-top) 0%,#e2d3f8 55%,var(--card-bottom) 100%)}
.card-mark{position:absolute;font-weight:700;white-space:nowrap}
.card-mark--gray{left:27px;top:30px;font-size:24px;color:#b3b0b8;letter-spacing:-1px}
.card-mark--blue{left:30px;top:24px;display:flex;align-items:center;gap:8px;font-size:15px;color:#3763b8}
.card-mark--blue i{display:block;width:22px;height:22px;border-radius:50%;background:#c53a3a}
.card-mark--brand{left:36px;top:34px;display:flex;align-items:center;gap:8px;font-size:17px;color:var(--mark)}
.card-mark--brand i{display:block;width:24px;height:24px;background:var(--mark)}
.card-title{position:absolute;font-size:18px;font-weight:500;white-space:nowrap}
.card-label{position:absolute;left:430px;font-size:18px;font-weight:500}
.add-btn{position:absolute;left:734px;width:198px;height:42px;border-radius:22px;background:var(--brand);color:var(--white);font-size:15px;font-weight:600;display:flex;align-items:center;justify-content:center;gap:10px;white-space:nowrap}
.add-btn::after{content:"";border-left:3px solid transparent;border-right:3px solid transparent;border-top:4px solid var(--white)}
.card-rule{position:absolute;left:25px;width:910px;height:1px;background:#b9a5dc}
.empty{position:absolute;left:0;width:100%;text-align:center;font-size:13px;color:var(--brand)}

.table{position:absolute;left:25px;top:157px;width:910px;border:1px solid #b9a5dc;font-size:13px}
.tr{display:flex;height:34px;border-bottom:1px solid #b9a5dc}
.tr > div{border-right:1px solid #b9a5dc;display:flex;align-items:center;justify-content:center;white-space:nowrap}
.tr > div:last-child{border-right:none}
.c1{width:208px}.c2{width:138px}.c3{width:160px}.c4{width:231px}.c5{width:173px}
.tr--head{background:var(--head-tint);font-weight:500}
.tr--filter{background:#e7dcf8;color:var(--brand)}
.tr--filter svg{width:14px;height:14px}
.tr--tint{background:var(--row-tint)}
.tr--plain{background:var(--white)}
.tr .name{justify-content:flex-start;padding-left:28px;gap:9px;font-size:12.5px;color:#333}
.tr .name::before{content:"";border-top:3px solid transparent;border-bottom:3px solid transparent;border-left:4px solid #333}
.tr .act{justify-content:flex-end;padding-right:12px}
.pill{width:109px;height:22px;border-radius:11px;background:var(--brand);color:var(--white);font-size:11px;font-weight:700;display:flex;align-items:center;justify-content:center;gap:8px}
.pill::after{content:"";width:4px;height:4px;border-radius:50%;background:var(--white)}
.tr--spacer{height:33px;border-bottom:none;background:transparent}

.footer{position:absolute;top:1043px;left:308px;width:960px;text-align:center;font-size:14.5px;color:#555;white-space:nowrap}
.code{position:absolute;left:1252px;top:1071px;font-size:11px;color:#444}

.menu{position:absolute;left:1035px;top:124px;width:211px;height:145px;background:var(--white);border:3px solid #6b2fd8;border-top-width:4px;padding:34px 0 0 24px}
.menu-item{display:flex;align-items:center;gap:10px;height:29px;font-size:15px;color:#222;white-space:nowrap}
.menu-item svg{width:17px;height:17px;fill:none;stroke:#444;stroke-width:1.5}
</style>
</head>
<body>
<div class="viewport">
<div class="stage">

<svg class="icon-defs" aria-hidden="true">
  <defs>
    <symbol id="i-search" viewBox="0 0 16 16"><circle cx="6.5" cy="6.5" r="4.5" fill="none" stroke="currentColor" stroke-width="2.2"/><path d="M10 10l4 4" stroke="currentColor" stroke-width="2.4" stroke-linecap="round"/></symbol>
    <symbol id="i-home" viewBox="0 0 20 20"><path d="M10 2L1 10h3v8h5v-5h2v5h5v-8h3z"/></symbol>
    <symbol id="i-grid" viewBox="0 0 20 20"><path d="M2 2h4v4H2zM8 2h4v4H8zM14 2h4v4h-4zM2 8h4v4H2zM8 8h4v4H8zM14 8h4v4h-4zM2 14h4v4H2zM8 14h4v4H8zM14 14h4v4h-4z"/></symbol>
    <symbol id="i-pencil" viewBox="0 0 20 20"><path d="M13 2l5 5-10 10H3v-5zM2 18h4l-4-4z"/></symbol>
    <symbol id="i-monitor" viewBox="0 0 20 20"><path d="M1 3h18v11H1zM3 5v7h14V5zM7 15h6v2h2v1H5v-1h2z"/></symbol>
  </defs>
</svg>

<section class="screen screen--one">
  <aside class="sidebar">
    <div class="nav-item nav-item--active" style="top:145px"><svg><use href="#i-home"/></svg>DASHBOARD</div>
    <div class="nav-item" style="top:202px"><svg><use href="#i-grid"/></svg>APPLICATIONS</div>
    <div class="nav-item" style="top:259px"><svg><use href="#i-pencil"/></svg>TRANSCRIPT REQUEST</div>
    <div class="nav-item" style="top:315px"><svg><use href="#i-monitor"/></svg>NEW HIRE PACKET</div>
  </aside>
  <header class="topbar">
    <div class="brand"><span class="brand-square"></span>Northfield Learning</div>
    <div class="search">Search<span class="search-btn"><svg><use href="#i-search"/></svg></span></div>
    <div class="avatar" role="img" aria-label="User profile photo"></div>
    <div class="user">Dana.M</div>
    <div class="caret"></div>
  </header>

  <article class="card" style="top:167px;height:164px">
    <div class="card-mark card-mark--gray">NLDEMO19</div>
    <div class="card-title" style="left:25px;top:84px">NLDEMO 19</div>
    <div class="card-label" style="top:85px">Students</div>
    <div class="add-btn" style="top:66px">Add students via..</div>
    <div class="card-rule" style="top:114px"></div>
    <div class="empty" style="top:134px">No Record Found</div>
  </article>

  <article class="card" style="top:344px;height:167px">
    <div class="card-mark card-mark--blue"><i></i>Ridgeway</div>
    <div class="card-title" style="left:53px;top:76px">RCCS</div>
    <div class="card-label" style="top:77px">Students</div>
    <div class="add-btn" style="top:66px">Add students via..</div>
    <div class="card-rule" style="top:117px"></div>
    <div class="empty" style="top:136px">No Record Found</div>
  </article>

  <article class="card" style="top:525px;height:466px">
    <div class="card-mark card-mark--brand"><i></i>Northfield Learning</div>
    <div class="card-title" style="left:53px;top:102px">Gradeline Demo Test</div>
    <div class="card-label" style="top:103px;left:405px">Students</div>
    <div class="add-btn" style="top:92px">Add students via..</div>
    <div class="table">
      <div class="tr tr--head"><div class="c1" style="justify-content:flex-start;padding-left:27px">NAME</div><div class="c2">GRADE</div><div class="c3">YEAR</div><div class="c4">SCHOOL/BUILDING</div><div class="c5">ACTIONS</div></div>
      <div class="tr tr--filter"><div class="c1" style="justify-content:flex-start;padding-left:41px"><svg><use href="#i-search"/></svg></div><div class="c2"><svg><use href="#i-search"/></svg></div><div class="c3"><svg><use href="#i-search"/></svg></div><div class="c4"><svg><use href="#i-search"/></svg></div><div class="c5"></div></div>
      <div class="tr tr--tint"><div class="c1 name">NLVIEW 8108</div><div class="c2">KG</div><div class="c3"></div><div class="c4">Testing</div><div class="c5 act"><span class="pill">Create/List</span></div></div>
      <div class="tr tr--plain"><div class="c1 name">Maren ostby</div><div class="c2"></div><div class="c3"></div><div class="c4">tstdt</div><div class="c5 act"><span class="pill">Create/List</span></div></div>
      <div class="tr tr--tint"><div class="c1 name">Tamsin j Ostby</div><div class="c2"></div><div class="c3"></div><div class="c4"></div><div class="c5 act"><span class="pill">Create/List</span></div></div>
      <div class="tr tr--plain"><div class="c1 name">Regression Test Test</div><div class="c2"></div><div class="c3"></div><div class="c4"></div><div class="c5 act"><span class="pill">Create/List</span></div></div>
      <div class="tr tr--tint"><div class="c1 name">Test Test</div><div class="c2">09</div><div class="c3">2024</div><div class="c4">Maple Ridge high School</div><div class="c5 act"><span class="pill">Create/List</span></div></div>
      <div class="tr tr--plain"><div class="c1 name">Rowan Ellis Parker</div><div class="c2"></div><div class="c3"></div><div class="c4">Testing</div><div class="c5 act"><span class="pill">Create/List</span></div></div>
      <div class="tr tr--spacer"><div class="c1"></div><div class="c2"></div><div class="c3"></div><div class="c4"></div><div class="c5"></div></div>
    </div>
  </article>

  <footer class="footer">© 2025 Companyname.All Rights Reserved &nbsp;|&nbsp; Privacy Policy &nbsp;|&nbsp; Terms of Use</footer>
  <div class="code">C9</div>
</section>

<section class="screen screen--two">
  <aside class="sidebar">
    <div class="nav-item nav-item--active" style="top:145px"><svg><use href="#i-home"/></svg>DASHBOARD</div>
    <div class="nav-item" style="top:202px"><svg><use href="#i-grid"/></svg>APPLICATIONS</div>
    <div class="nav-item" style="top:259px"><svg><use href="#i-pencil"/></svg>TRANSCRIPT REQUEST</div>
    <div class="nav-item" style="top:315px"><svg><use href="#i-monitor"/></svg>NEW HIRE PACKET</div>
  </aside>
  <header class="topbar">
    <div class="brand"><span class="brand-square"></span>Northfield Learning</div>
    <div class="search">Search<span class="search-btn"><svg><use href="#i-search"/></svg></span></div>
    <div class="avatar" role="img" aria-label="User profile photo"></div>
    <div class="user">Dana.M</div>
    <div class="caret"></div>
  </header>

  <article class="card" style="top:167px;height:164px">
    <div class="card-mark card-mark--gray">NLDEMO19</div>
    <div class="card-title" style="left:25px;top:84px">NLDEMO 19</div>
    <div class="card-label" style="top:85px">Students</div>
    <div class="add-btn" style="top:66px">Add students via..</div>
    <div class="card-rule" style="top:114px"></div>
    <div class="empty" style="top:134px">No Record Found</div>
  </article>

  <article class="card" style="top:344px;height:167px">
    <div class="card-mark card-mark--blue"><i></i>Ridgeway</div>
    <div class="card-title" style="left:53px;top:76px">RCCS</div>
    <div class="card-label" style="top:77px">Students</div>
    <div class="add-btn" style="top:66px">Add students via..</div>
    <div class="card-rule" style="top:117px"></div>
    <div class="empty" style="top:136px">No Record Found</div>
  </article>

  <article class="card" style="top:525px;height:466px">
    <div class="card-mark card-mark--brand"><i></i>Northfield Learning</div>
    <div class="card-title" style="left:53px;top:102px">Gradeline Demo Test</div>
    <div class="card-label" style="top:103px;left:405px">Students</div>
    <div class="add-btn" style="top:92px">Add students via..</div>
    <div class="table">
      <div class="tr tr--head"><div class="c1" style="justify-content:flex-start;padding-left:27px">NAME</div><div class="c2">GRADE</div><div class="c3">YEAR</div><div class="c4">SCHOOL/BUILDING</div><div class="c5">ACTIONS</div></div>
      <div class="tr tr--filter"><div class="c1" style="justify-content:flex-start;padding-left:41px"><svg><use href="#i-search"/></svg></div><div class="c2"><svg><use href="#i-search"/></svg></div><div class="c3"><svg><use href="#i-search"/></svg></div><div class="c4"><svg><use href="#i-search"/></svg></div><div class="c5"></div></div>
      <div class="tr tr--tint"><div class="c1 name">NLVIEW 8108</div><div class="c2">KG</div><div class="c3"></div><div class="c4">Testing</div><div class="c5 act"><span class="pill">Create/List</span></div></div>
      <div class="tr tr--plain"><div class="c1 name">Maren ostby</div><div class="c2"></div><div class="c3"></div><div class="c4">tstdt</div><div class="c5 act"><span class="pill">Create/List</span></div></div>
      <div class="tr tr--tint"><div class="c1 name">Tamsin j Ostby</div><div class="c2"></div><div class="c3"></div><div class="c4"></div><div class="c5 act"><span class="pill">Create/List</span></div></div>
      <div class="tr tr--plain"><div class="c1 name">Regression Test Test</div><div class="c2"></div><div class="c3"></div><div class="c4"></div><div class="c5 act"><span class="pill">Create/List</span></div></div>
      <div class="tr tr--tint"><div class="c1 name">Test Test</div><div class="c2">09</div><div class="c3">2024</div><div class="c4">Maple Ridge high School</div><div class="c5 act"><span class="pill">Create/List</span></div></div>
      <div class="tr tr--plain"><div class="c1 name">Rowan Ellis Parker</div><div class="c2"></div><div class="c3"></div><div class="c4">Testing</div><div class="c5 act"><span class="pill">Create/List</span></div></div>
      <div class="tr tr--spacer"><div class="c1"></div><div class="c2"></div><div class="c3"></div><div class="c4"></div><div class="c5"></div></div>
    </div>
  </article>

  <nav class="menu" aria-label="Profile menu">
    <div class="menu-item"><svg viewBox="0 0 18 18"><circle cx="9" cy="6" r="3.5"/><path d="M2.5 16.5c0-3.5 3-5.5 6.5-5.5s6.5 2 6.5 5.5z"/></svg>My Profile</div>
    <div class="menu-item"><svg viewBox="0 0 18 18"><rect x="3" y="8" width="12" height="8.5" rx="1"/><path d="M5.5 8V5.5a3.5 3.5 0 017 0V8"/></svg>Change Password</div>
    <div class="menu-item"><svg viewBox="0 0 18 18"><path d="M7 2.5H3v13h4M7 9h9M13 6l3 3-3 3"/></svg>Logout</div>
  </nav>

  <footer class="footer">© 2025 Companyname.All Rights Reserved &nbsp;|&nbsp; Privacy Policy &nbsp;|&nbsp; Terms of Use</footer>
  <div class="code">C9</div>
</section>

</div>
</div>
</body>
</html>
```